A-Stand Directional Sign Design

Objective:
We need a professional graphic design for an A-Stand sign that will guide customers arriving in our parking lot to our office. The design should be visually clear, welcoming, and aligned with our brand identity.
REQUIREMENTS:
Two versions of the design:
- One with an arrow pointing left
- One with an arrow pointing right
(This allows us to place the A-Stand anywhere and flip the graphic as needed.)
DIMENSIONS:
- Viewable Area: 30" x 40"
BRAND ALIGNMENT:
- Colors, fonts, and overall style should match our website: www.skornabel.com
- Clean, modern, and professional look consistent with our aviation/tourism brand
CONTENT:
- Clear directional arrow (left or right depending on version)
- Text: “Office Entrance” or similar concise wording (designers may propose alternatives if they improve clarity)
READABILITY:
- Bold, high-contrast design for visibility from a distance
- Simple layout that avoids clutter
DELIVERABLES:
- Final artwork in print-ready format (PDF preferred)
- Two versions: Arrow Left and Arrow Right
DESIGN GOAL:
Ensure customers can easily find our office upon arrival, while reinforcing skorNABEL’s professional and welcoming brand image.
Target Market(s)
Tourism

```html
<!DOCTYPE html>
<html lang="en">
<head>
<meta charset="utf-8">
<title>skorNABEL – Office Entrance A-Stand</title>
<link rel="stylesheet" href="https://fonts.googleapis.com/css2?family=Lato:wght@700;900&display=swap">
<style>
  :root {
    --brand-blue: #2276ba;
    --brand-blue-light: #8aafd9;
    --ink: #0b0b0b;
    --paper: #ffffff;
    --backdrop: #e1e7ef;
    --photo-sky: #7fb6cf;
    --photo-sea: #3f6f85;
    --photo-cabin: #c9a98a;
    --photo-cabin-dark: #5a4a40;
  }
  * { box-sizing: border-box; margin: 0; padding: 0; }
  html, body {
    width: 1200px;
    height: 2309px;
    overflow: hidden;
    background: var(--backdrop);
    font-family: "Lato", Arial, sans-serif;
  }
  .sign {
    position: absolute;
    left: 60px;
    top: 434px;
    width: 900px;
    height: 1200px;
    transform: scale(1.2);
    transform-origin: top left;
    background: var(--paper);
  }
  .brand {
    position: absolute;
    left: 0;
    top: 90px;
    width: 100%;
    display: flex;
    flex-direction: column;
    align-items: center;
    gap: 46px;
  }
  .brand-dot {
    width: 190px;
    height: 190px;
    border-radius: 50%;
    background: var(--brand-blue);
  }
  .brand-name {
    font-weight: 900;
    font-size: 104px;
    line-height: 1;
    color: var(--brand-blue);
    letter-spacing: 1px;
  }
  .gallery {
    position: absolute;
    top: 515px;
    left: 65px;
    display: flex;
    gap: 28px;
  }
  .gallery-photo {
    width: 355px;
    height: 355px;
    border: 14px solid var(--brand-blue);
  }
  .photo-pilot {
    background: linear-gradient(180deg, var(--photo-sky) 0%, #b9d8e4 35%, var(--photo-sea) 70%, #2b3a42 100%);
  }
  .photo-passengers {
    background: linear-gradient(160deg, var(--photo-cabin) 0%, #e6d3bd 45%, var(--photo-cabin-dark) 100%);
  }
  .direction-label {
    position: absolute;
    left: 66px;
    top: 895px;
    font-weight: 900;
    font-size: 62px;
    line-height: 74px;
    color: var(--ink);
    text-transform: uppercase;
  }
  .direction-arrow {
    position: absolute;
    left: 522px;
    top: 882px;
    width: 314px;
    height: 178px;
  }
  .web-band {
    position: absolute;
    left: 0;
    top: 1070px;
    width: 100%;
    height: 82px;
    background: var(--brand-blue);
    display: flex;
    align-items: center;
    justify-content: center;
  }
  .web-address {
    font-weight: 900;
    font-size: 42px;
    color: var(--paper);
  }
</style>
</head>
<body>
  <main class="sign">
    <header class="brand">
      <div class="brand-dot"></div>
      <div class="brand-name">skorNABEL.com</div>
    </header>

    <section class="gallery">
      <div class="gallery-photo photo-pilot" role="img" aria-label="Pilot with headset flying a helicopter over a coastal city"></div>
      <div class="gallery-photo photo-passengers" role="img" aria-label="Smiling couple wearing headsets inside a helicopter cabin"></div>
    </section>

    <h1 class="direction-label">Office<br>Entrance</h1>

    <svg class="direction-arrow" viewBox="0 0 314 178" aria-hidden="true">
      <polygon points="0,43 230,43 230,0 314,89 230,178 230,134 0,134" fill="var(--brand-blue)"/>
    </svg>

    <footer class="web-band">
      <span class="web-address">www.skornabel.com</span>
    </footer>
  </main>
</body>
</html>
```